Business Card Design Project - bel soravin group

dear Sirs

we need business card design for our group ( BEL Soravin Group ) , i have got the Logo design of our group from pixel harbor in previous , so all need details relating to our group i think available with you, as well as the the chosen logo design

we hope to provide us with business card logo that to be appropaite and satisfactory to us .

thanks

note : logo design of our group is attached .
Updates

Reason: please extend the deadline of my project for additional 15 days because i didn't received appropriate design for our gruop yet . kindly beaware that i have received 77 design till now , supossed to send me 200-250 design at least . thanks

Target Market(s)

contents
-

name : Korvan EL Mistrani

position : Operation Manager

Industry/Entity Type

Business

Requirements
Must have

• person name

group logo
Nice to have
• logo color matching with back background

```html
<!DOCTYPE html>
<html lang="en">
<head>
<meta charset="utf-8">
<title>BEL Soravin Group – Business Card</title>
<link rel="stylesheet" href="https://fonts.googleapis.com/css2?family=Ubuntu:wght@400;500;700&display=swap">
<style>
  :root {
    --page-bg: #e9ecef;
    --card-blue: #1d5791;
    --logo-tint: #86a9cf;
    --band-white: #ffffff;
    --name-blue: #1d5791;
    --ink-dark: #1b1b1b;
    --text-white: #ffffff;
  }
  * { margin: 0; padding: 0; box-sizing: border-box; }
  html, body {
    width: 1067px;
    height: 1200px;
    overflow: hidden;
    background: var(--page-bg);
    font-family: "Ubuntu", sans-serif;
  }
  .sheet {
    position: relative;
    width: 1067px;
    height: 1200px;
  }
  .card {
    position: absolute;
    left: 103px;
    width: 860px;
    height: 490px;
    background: var(--card-blue);
    overflow: hidden;
    box-shadow: 0 6px 18px rgba(0,0,0,0.18);
  }
  .card--front { top: 80px; }
  .card--back { top: 630px; }
  .front__brand {
    position: absolute;
    left: 72px;
    top: 245px;
    transform: translate(-50%, -50%) rotate(-90deg);
    white-space: nowrap;
    display: flex;
    align-items: center;
    gap: 14px;
    color: var(--logo-tint);
    font-weight: 400;
    font-size: 44px;
    letter-spacing: 1px;
  }
  .brand-mark {
    width: 26px;
    height: 26px;
    border: 3px solid var(--logo-tint);
  }
  .name-band {
    position: absolute;
    left: 290px;
    top: 176px;
    right: 0;
    height: 118px;
    background: var(--band-white);
    border-radius: 22px 0 0 22px;
    padding: 26px 0 0 34px;
  }
  .name-band__name {
    color: var(--name-blue);
    font-size: 40px;
    font-weight: 400;
    line-height: 1;
  }
  .name-band__role {
    margin-top: 8px;
    color: var(--ink-dark);
    font-size: 15px;
    font-weight: 700;
  }
  .contact {
    position: absolute;
    right: 30px;
    top: 314px;
    list-style: none;
    text-align: right;
    color: var(--text-white);
    font-size: 23px;
    line-height: 33px;
  }
  .back__brand {
    position: absolute;
    left: 50%;
    top: 222px;
    transform: translate(-50%, -50%);
    white-space: nowrap;
    display: flex;
    align-items: center;
    gap: 18px;
    color: var(--logo-tint);
    font-weight: 400;
    font-size: 50px;
    letter-spacing: 1px;
  }
  .back__brand .brand-mark { width: 30px; height: 30px; }
</style>
</head>
<body>
<main class="sheet">

  <section class="card card--front" aria-label="Business card front">
    <div class="front__brand">
      <span class="brand-mark"></span>
      <span>BEL Soravin Group</span>
    </div>
    <div class="name-band">
      <p class="name-band__name">Korvan EL Mistrani</p>
      <p class="name-band__role">Operation Manager</p>
    </div>
    <ul class="contact">
      <li>Phone: 0123 456 789</li>
      <li>Fax: 0123 456 789</li>
      <li>info@yourdomain.com</li>
      <li>www.yourdomain.com</li>
      <li>PO. Box: City name, etc.</li>
    </ul>
  </section>

  <section class="card card--back" aria-label="Business card back">
    <div class="back__brand">
      <span class="brand-mark"></span>
      <span>BEL Soravin Group</span>
    </div>
  </section>

</main>
</body>
</html>
```